Kestrel Path Business card

We are a company that owns 2 compliance software programs for TV, Radio and Cable industries as well as an online job board. We need a professional business card that incorproates all three logos.

```html
<!DOCTYPE html>
<html lang="en">
<head>
<meta charset="utf-8">
<title>Kestrel Path Business Card</title>
<link rel="stylesheet" href="https://fonts.googleapis.com/css2?family=Roboto:wght@400;500&family=Roboto+Condensed:wght@700&display=swap">
<style>
  :root {
    --backdrop: #2b2b2d;
    --card: #ffffff;
    --card-back-tint: #f6f6f8;
    --navy: #2b2a6e;
    --orange: #ef4423;
    --blue: #2e8fd6;
  }
  * { margin: 0; padding: 0; box-sizing: border-box; }
  html, body { width: 1200px; height: 880px; overflow: hidden; }
  body {
    background: var(--backdrop);
    position: relative;
    font-family: "Roboto", Arial, sans-serif;
  }
  .card {
    position: absolute;
    width: 620px;
    height: 354px;
    border-radius: 22px;
    overflow: hidden;
    background: var(--card);
    box-shadow: 0 10px 28px rgba(0,0,0,.45);
  }
  .card--back {
    left: 90px; top: 50px;
    background: linear-gradient(135deg, var(--card) 0%, var(--card-back-tint) 100%);
  }
  .card--front { left: 490px; top: 470px; }

  .brand-row {
    position: absolute;
    display: flex;
    align-items: center;
    gap: 14px;
  }
  .card--back .brand-row { left: 50%; top: 50%; transform: translate(-50%, -50%); }
  .card--front .brand-row { left: 40px; right: 40px; top: 56px; justify-content: space-between; gap: 0; }

  .brand {
    font-family: "Roboto Condensed", Arial, sans-serif;
    font-weight: 700;
    font-size: 18px;
    color: var(--navy);
    display: flex;
    align-items: center;
    gap: 6px;
    white-space: nowrap;
  }
  .brand__dot {
    width: 10px; height: 10px;
    border-radius: 50%;
    background: var(--orange);
  }
  .brand__dot--blue { background: var(--blue); }
  .brand-divider {
    width: 2px; height: 56px;
    background: var(--navy);
  }

  .person {
    position: absolute;
    right: 304px; top: 222px;
    text-align: right;
  }
  .person__name {
    font-family: "Roboto Condensed", Arial, sans-serif;
    font-weight: 700;
    font-size: 28px;
    color: var(--navy);
    letter-spacing: .5px;
    line-height: 1;
    white-space: nowrap;
  }
  .person__title {
    font-size: 16px;
    color: var(--orange);
    margin-top: 4px;
  }
  .contact-divider {
    position: absolute;
    left: 336px; top: 200px;
    width: 2px; height: 78px;
    background: var(--navy);
  }
  .contact {
    position: absolute;
    left: 356px; top: 202px;
    list-style: none;
  }
  .contact__item {
    display: flex;
    align-items: center;
    gap: 8px;
    font-size: 15px;
    color: var(--navy);
    line-height: 25px;
    white-space: nowrap;
  }
  .contact__item svg { width: 14px; height: 14px; flex: none; }

  .card__band {
    position: absolute;
    left: 0; right: 0; bottom: 0;
    height: 9px;
    display: flex;
  }
  .card__band-navy { width: 48%; background: var(--navy); }
  .card__band-orange { flex: 1; background: var(--orange); }
</style>
</head>
<body>

  <section class="card card--back" aria-label="Card back">
    <div class="brand-row">
      <span class="brand"><span class="brand__dot"></span>Airwave Ledger</span>
      <span class="brand-divider"></span>
      <span class="brand"><span class="brand__dot"></span>Cableline Ledger</span>
      <span class="brand-divider"></span>
      <span class="brand"><span class="brand__dot brand__dot--blue"></span>CrewBoardNow.com</span>
    </div>
  </section>

  <section class="card card--front" aria-label="Card front">
    <div class="brand-row">
      <span class="brand"><span class="brand__dot"></span>Airwave Ledger</span>
      <span class="brand-divider"></span>
      <span class="brand"><span class="brand__dot"></span>Cableline Ledger</span>
      <span class="brand-divider"></span>
      <span class="brand"><span class="brand__dot brand__dot--blue"></span>CrewBoardNow.com</span>
    </div>

    <div class="person">
      <p class="person__name">ALEX MORGAN</p>
      <p class="person__title">Director</p>
    </div>

    <span class="contact-divider"></span>

    <ul class="contact">
      <li class="contact__item">
        <svg viewBox="0 0 14 14" aria-hidden="true"><rect x="3" y="1" width="8" height="12" rx="1.5" fill="none" stroke="#ef4423" stroke-width="1.6"/></svg>
        (555) 014 2280
      </li>
      <li class="contact__item">
        <svg viewBox="0 0 14 14" aria-hidden="true"><rect x="1" y="3" width="12" height="8" fill="#ef4423"/><path d="M1 3 L7 8 L13 3" fill="none" stroke="#fff" stroke-width="1.2"/></svg>
        hello@kestrelpath.com
      </li>
      <li class="contact__item">
        <svg viewBox="0 0 14 14" aria-hidden="true"><circle cx="7" cy="7" r="5.5" fill="none" stroke="#ef4423" stroke-width="1.4"/><ellipse cx="7" cy="7" rx="2.3" ry="5.5" fill="none" stroke="#ef4423" stroke-width="1.1"/><path d="M1.5 7 H12.5" stroke="#ef4423" stroke-width="1.1"/></svg>
        www.kestrelpath.com
      </li>
    </ul>

    <div class="card__band" aria-hidden="true">
      <span class="card__band-navy"></span>
      <span class="card__band-orange"></span>
    </div>
  </section>

</body>
</html>
```